Design a certificate for our Course

Points to consider

*Size of the Certificate: Legal Size
*Name Of the Course: Professional Diploma in Web Designing & Development
*Course Provider: Velon Learning Institute (VeLI)
*Subsidiary: VeLI is a subsidiary of Korvath Software Solutions (PVT) LTD
*Primary Logo on the Top: VeLI logo (attached - remove the shadow on the bottom)
*Subsidiary Logo should be put on the bottom: Korvath Software Solutions Logo (attached)

2 signatories

*Signatory on the left side:

T.J. Dulmin Perera
CEO, Korvath Software Solutions
B. Sc. (Eng) Hons.
(Computer Science & Engineering
University of Kelbrook),
MBA (University of Tarnsey),

A scanned image of the signature will be provided for the selected candidate to attach to the signature column

Signatory on the right side:
S.K. Nuwanthaka Silva,
CEO, Velon Learning Institute,
FRQP - UK, M.Sc in Information Security (Orient Q College - Malaysia)

Company registration number : PV58917

```html
<!DOCTYPE html>
<html lang="en">
<head>
<meta charset="utf-8">
<title>Certificate of Completion – Velon Learning Institute</title>
<link rel="stylesheet" href="https://fonts.googleapis.com/css2?family=Almendra+SC&family=Tinos:ital@0;1&family=Oswald:wght@700&family=Open+Sans:wght@400;700&display=swap">
<style>
  :root {
    --paper: #e3e6e8;
    --frame: #2b2b2d;
    --frame-light: #5a5a5e;
    --ink: #1c1c1e;
    --rule: #8d9094;
    --course-blue: #5a4fdf;
    --sub-blue: #3b3cbc;
    --wave: #c9ccd0;
  }
  * { margin: 0; padding: 0; box-sizing: border-box; }
  html, body { width: 928px; height: 1200px; overflow: hidden; background: #ffffff; }
  .certificate {
    position: relative;
    width: 928px;
    height: 1200px;
    background: var(--paper);
    font-family: "Tinos", "Times New Roman", serif;
    color: var(--ink);
    overflow: hidden;
  }
  .certificate__wave {
    position: absolute;
    left: 770px; top: 90px;
    width: 100px; height: 1020px;
    background: linear-gradient(90deg, rgba(201,204,208,0) 0%, var(--wave) 55%, rgba(201,204,208,0.2) 100%);
    opacity: 0.7;
  }
  .certificate__star {
    position: absolute;
    left: 370px; top: 360px;
    width: 250px; height: 210px;
    background: radial-gradient(ellipse at center, rgba(226,214,150,0.35) 0%, rgba(226,214,150,0) 70%);
  }
  .certificate__frame { position: absolute; inset: 0; }
  .brand {
    position: absolute;
    top: 112px; left: 0; right: 0;
    text-align: center;
  }
  .brand__name {
    font-family: "Open Sans", Arial, sans-serif;
    font-weight: 700;
    font-size: 34px;
    line-height: 1;
    letter-spacing: 1px;
    color: var(--ink);
  }
  .title {
    position: absolute;
    top: 226px; left: 0; right: 0;
    text-align: center;
    font-family: "Almendra SC", "Times New Roman", serif;
    font-size: 54px;
    font-weight: 400;
    letter-spacing: 1px;
    color: #262628;
    text-shadow: 2px 3px 3px rgba(0,0,0,0.45);
    white-space: nowrap;
  }
  .line-text {
    position: absolute; left: 0; right: 0;
    text-align: center;
    font-size: 31px;
  }
  .line-text--certifies { top: 342px; }
  .line-text--completed { top: 487px; }
  .recipient-rule {
    position: absolute;
    left: 162px; top: 448px;
    width: 578px; height: 1px;
    background: var(--rule);
  }
  .course {
    position: absolute;
    top: 566px; left: 50%;
    width: max-content;
    font-family: "Oswald", "Arial Narrow", sans-serif;
    font-weight: 700;
    font-size: 40px;
    line-height: 1.2;
    color: var(--course-blue);
    white-space: nowrap;
    transform: translateX(-50%) scaleX(0.82);
  }
  .awarded {
    position: absolute;
    top: 658px; left: 266px;
    display: flex; align-items: flex-end; gap: 14px;
    font-style: italic;
    font-size: 31px;
  }
  .awarded__date {
    display: flex; width: 198px;
    border-bottom: 1px solid var(--rule);
    height: 34px;
    font-style: normal;
    font-size: 28px;
    color: var(--rule);
  }
  .awarded__date span:first-child { margin-left: 50px; }
  .awarded__date span:last-child { margin-left: 40px; }
  .signatory {
    position: absolute;
    top: 835px;
    font-family: "Open Sans", Arial, sans-serif;
    text-transform: uppercase;
    border-top: 1px solid var(--rule);
  }
  .signatory--left { left: 82px; width: 268px; }
  .signatory--right { left: 551px; width: 297px; text-align: right; }
  .signatory--right .signatory__name,
  .signatory--right .signatory__details { margin-right: 22px; }
  .signatory__name {
    margin-top: 18px;
    font-weight: 700;
    font-size: 18px;
    line-height: 24px;
  }
  .signatory__details {
    margin-top: 10px;
    font-size: 14px;
    line-height: 26.5px;
    white-space: nowrap;
  }
  .subsidiary {
    position: absolute;
    top: 1036px; left: 350px;
    display: flex; align-items: center; gap: 10px;
  }
  .subsidiary__dot {
    width: 30px; height: 30px; border-radius: 50%;
    background: var(--sub-blue);
  }
  .subsidiary__name {
    font-family: "Open Sans", Arial, sans-serif;
    font-weight: 700;
    font-size: 21px;
    color: var(--sub-blue);
  }
</style>
</head>
<body>
<main class="certificate">
  <div class="certificate__wave" role="img" aria-label="Flowing grey line pattern down the right edge"></div>
  <div class="certificate__star" role="img" aria-label="Faint gold line star behind the recipient name"></div>

  <svg class="certificate__frame" width="928" height="1200" viewBox="0 0 928 1200" role="img" aria-label="Dark ornamental border with corner blocks">
    <rect x="6" y="6" width="916" height="1188" fill="none" stroke="var(--frame-light)" stroke-width="2"/>
    <path fill="var(--frame)" fill-rule="evenodd" d="M16 12 H912 V1188 H16 Z M52 48 V1152 H876 V48 Z"/>
    <rect x="56" y="52" width="816" height="1096" fill="none" stroke="var(--frame)" stroke-width="2"/>
    <rect x="4" y="4" width="90" height="86" fill="var(--frame)"/>
    <rect x="834" y="4" width="90" height="86" fill="var(--frame)"/>
    <rect x="4" y="1110" width="90" height="86" fill="var(--frame)"/>
    <rect x="834" y="1110" width="90" height="86" fill="var(--frame)"/>
  </svg>

  <header class="brand">
    <span class="brand__name">VELON LEARNING INSTITUTE</span>
  </header>

  <h1 class="title">CERTIFICATE OF COMPLETION</h1>

  <p class="line-text line-text--certifies">This certifies that</p>
  <div class="recipient-rule"></div>
  <p class="line-text line-text--completed">has successfully completed the course of</p>

  <h2 class="course">PROFESSIONAL DIPLOMA IN WEB DESIGNING &amp; DEVELOPMENT</h2>

  <div class="awarded">
    <span>Awarded On:</span>
    <span class="awarded__date"><span>/</span><span>/</span></span>
  </div>

  <section class="signatory signatory--left">
    <p class="signatory__name">T.J. Dulmin Perera</p>
    <p class="signatory__details">
      CEO, Korvath Software Solutions<br>
      B. Sc. (Eng) Hons.<br>
      (Computer Science &amp; Engineering<br>
      University of Kelbrook),<br>
      MBA (University of Tarnsey)
    </p>
  </section>

  <section class="signatory signatory--right">
    <p class="signatory__name">S.K. Nuwanthaka Silva</p>
    <p class="signatory__details">
      CEO, Velon Learning Institute,<br>
      FRQP - UK, M.Sc in Information Security<br>
      (Orient Q College - Malaysia)
    </p>
  </section>

  <footer class="subsidiary">
    <span class="subsidiary__dot"></span>
    <span class="subsidiary__name">Korvath Software Solutions</span>
  </footer>
</main>
</body>
</html>
```